Flyer for swimming pool service business

I am starting up a new pool cleaning business and I'm focusing on suburbs surrounding my suburb. So it will be a local service with fast, professional and friendly service.. I would like a Flyer of A5 size to drop into letterboxes local homes.

The business is called 'Gumtree Spa Care'

The following is what I would like in the flyer

Pool service frustrating you?
Troubled by poor water condition?
Tired of doing it yourself?

Keep your swimming pool sparkling and safe all year round

- water testing
- pool chemistry
- chlorine levels
- Ph balance
- equipment maintenance
- algae prevention
- leaf and debris maintenance
- filter cleaning
- tile cleaning
- salt water systems
- local service
- chemicals supplied and delivered
All for the low price of $40 a month (plus chemicals)

Relax and let Gumtree Spa Care take care of it for you.
for a one off service or a monthly service
no contracts

Contact details
Liam - 0417 382 604
gumtreespacare@westmail.net.au

Target Market(s)

the target market is a couples and familys 40-70 years old in a well off riverside suburb

Industry/Entity Type

Pool Service

Requirements
Must have
• Am looking to have a nice blue crystal clear water as part of the background either big or small.

Include my logo (provided) feel free to change the font of the Gumtree Spas Care writing on it, if that suits your design
Should not have
• cartoonish or funny images

```html
<!DOCTYPE html>
<html lang="en">
<head>
<meta charset="utf-8">
<title>Tallowood Spa Care – Flyer</title>
<link rel="stylesheet" href="https://fonts.googleapis.com/css2?family=Open+Sans:ital,wght@0,300;0,400;0,600;0,700;0,800;1,400&display=swap">
<style>
  :root {
    --backdrop: #2e2f31;
    --water-light: #4fb6e6;
    --water-mid: #1f86c8;
    --water-deep: #0d5c9e;
    --panel: rgba(20, 70, 170, 0.82);
    --panel-edge: rgba(255, 255, 255, 0.12);
    --white: #ffffff;
    --soft-white: rgba(255, 255, 255, 0.85);
    --rule: rgba(255, 255, 255, 0.6);
  }
  * { box-sizing: border-box; margin: 0; padding: 0; }
  html, body {
    width: 1200px; height: 793px; overflow: hidden;
    background: var(--backdrop);
    font-family: "Open Sans", Arial, sans-serif;
    color: var(--white);
  }
  .canvas { position: relative; width: 1200px; height: 793px; }

  .flyer {
    position: absolute; left: 338px; top: 26px;
    width: 524px; height: 741px; overflow: hidden;
  }
  .flyer__water {
    position: absolute; inset: 0;
    background:
      radial-gradient(ellipse at 30% 20%, var(--water-light) 0%, transparent 55%),
      radial-gradient(ellipse at 80% 85%, var(--water-light) 0%, transparent 45%),
      linear-gradient(160deg, var(--water-mid) 0%, var(--water-deep) 60%, var(--water-mid) 100%);
  }

  .panel {
    position: absolute; left: 24px; top: 26px; width: 476px; height: 592px;
    background: var(--panel);
    border: 1px solid var(--panel-edge);
    border-radius: 14px;
  }

  .brand { position: absolute; left: 24px; top: 24px; display: flex; align-items: center; }
  .brand__mark {
    width: 84px; height: 84px; border-radius: 50%;
    background: var(--white); flex: none;
  }
  .brand__name {
    margin-left: 36px; font-size: 23px; font-weight: 600; letter-spacing: 0.2px; white-space: nowrap;
  }
  .tagline {
    position: absolute; left: 198px; top: 88px; width: 260px;
    font-size: 7.5px; color: var(--soft-white);
  }

  .headline {
    position: absolute; left: 20px; top: 150px; width: 436px;
    text-align: center; font-size: 26px; font-weight: 400; line-height: 1.18;
  }

  .services {
    position: absolute; left: 40px; top: 264px; width: 410px;
    font-size: 12.5px; font-weight: 300; line-height: 1.4;
    text-align: justify; text-align-last: left;
  }
  .rule {
    position: absolute; left: 40px; top: 352px; width: 410px; height: 1px;
    background: var(--rule);
  }

  .offer__lead {
    position: absolute; left: 22px; top: 360px;
    font-size: 40px; font-weight: 800; line-height: 1; letter-spacing: -0.5px;
  }
  .offer__sub {
    position: absolute; left: 22px; top: 402px;
    font-size: 22px; font-weight: 300; text-transform: uppercase; letter-spacing: -0.3px; white-space: nowrap;
  }
  .offer__currency {
    position: absolute; left: 188px; top: 446px;
    font-size: 58px; font-weight: 300; line-height: 1;
  }
  .offer__price {
    position: absolute; left: 220px; top: 378px;
    font-size: 172px; font-weight: 800; line-height: 1; letter-spacing: -6px;
  }
  .offer__term {
    position: absolute; right: 26px; top: 548px;
    font-size: 23px; font-weight: 800; white-space: nowrap;
  }
  .offer__term small { font-size: 17px; font-weight: 400; }

  .contact {
    position: absolute; left: 42px; top: 636px;
    font-size: 12.5px; line-height: 1.35;
  }
  .contact__title { font-weight: 700; font-size: 13px; }
  .terms {
    position: absolute; left: 292px; top: 660px; width: 190px;
    font-size: 11px; line-height: 1.35; color: var(--soft-white);
  }
</style>
</head>
<body>
<main class="canvas">
  <article class="flyer">
    <div class="flyer__water" role="img" aria-label="Crystal clear blue pool water with rippling light"></div>

    <section class="panel">
      <header class="brand">
        <span class="brand__mark"></span>
        <span class="brand__name">Tallowood Spa Care</span>
      </header>
      <p class="tagline">Keep your swimming pool sparkling and safe all year round</p>

      <h1 class="headline">Pool service frustrating you?<br>Troubled by poor water condition?<br>Tired of doing it yourself?</h1>

      <p class="services">- water testing &nbsp;- pool chemistry &nbsp;- chlorine levels &nbsp;- Ph balance - equipment maintenance &nbsp;- algae prevention &nbsp;- leaf and debris maintenance &nbsp;- filter cleaning &nbsp;- tile cleaning &nbsp;- salt water systems &nbsp;- local service &nbsp;- chemicals supplied and delivered</p>

      <div class="rule"></div>

      <p class="offer__lead">ALL FOR</p>
      <p class="offer__sub">The low price of</p>
      <span class="offer__currency">$</span>
      <span class="offer__price">40</span>
      <p class="offer__term">A MONTH <small>(plus chemicals)</small></p>
    </section>

    <footer class="contact">
      <p class="contact__title">Contact details</p>
      <p>Liam - 0491 570 156</p>
      <p>tallowoodspacare@example.com.au</p>
    </footer>
    <p class="terms">For a one off service or a monthly service no contracts.</p>
  </article>
</main>
</body>
</html>
```